Electrical needs letterhead design

Need a letterhead design for an electrical company. Using the same colours as to what are used in the logo.
After a modern design.

Want the logo in top right or top left.

Must include...

ABN 71 804 239 356
PHONE 0458203917
www.kelmaroo.com.au
jed@kelmaroo.com.au

'ABN' and 'PHONE' in bold.

Keep it basic. Logo top left, details either next to it or far right corner. Dont want any other objects included.

Electrical

```html
<!DOCTYPE html>
<html lang="en">
<head>
<meta charset="utf-8">
<title>Kelmaroo Letterhead</title>
<link rel="stylesheet" href="https://fonts.googleapis.com/css2?family=Montserrat:wght@400;500;700&display=swap">
<style>
  :root {
    --brand-red: #7c2629;
    --logo-red: #9a2a24;
    --paper: #ffffff;
    --detail-text: #f4eaea;
  }
  * { margin: 0; padding: 0; box-sizing: border-box; }
  html, body {
    width: 900px;
    height: 1200px;
    overflow: hidden;
    background: var(--paper);
  }
  .letterhead {
    position: relative;
    width: 900px;
    height: 1200px;
    background: var(--paper);
    font-family: "Montserrat", sans-serif;
  }
  .brand {
    position: absolute;
    left: 32px;
    top: 54px;
    width: 230px;
  }
  .brand-name {
    display: block;
    font-size: 44px;
    font-weight: 500;
    color: var(--logo-red);
    letter-spacing: -0.5px;
    line-height: 1;
  }
  .header-band {
    position: absolute;
    left: 276px;
    top: 0;
    width: 624px;
    height: 134px;
    background: var(--brand-red);
  }
  .contact-details {
    position: absolute;
    left: 395px;
    top: 26px;
    width: 220px;
    list-style: none;
    color: var(--detail-text);
    font-size: 14.5px;
    font-weight: 400;
    line-height: 24px;
    letter-spacing: 0.2px;
    white-space: nowrap;
  }
  .contact-label {
    font-weight: 700;
    display: inline-block;
  }
  .contact-label.abn { width: 62px; }
</style>
</head>
<body>
  <main class="letterhead">
    <div class="brand">
      <span class="brand-name">Kelmaroo</span>
    </div>
    <header class="header-band">
      <ul class="contact-details">
        <li><span class="contact-label abn">ABN</span>: 71 804 239 356</li>
        <li><span class="contact-label">PHONE</span> : 0458203917</li>
        <li>www.kelmaroo.com.au</li>
        <li>jed@kelmaroo.com.au</li>
      </ul>
    </header>
  </main>
</body>
</html>
```